IT Company based on Biology Business Needs a Business Card Design

We need a business card design for a new company called 'Lumen CELL'. We develop the machine learning solutions especially focused on deep learning algorithms for biology industry. Our initial product is a vision detection on biological images to help doctors diagnose the symptoms. We would like to see designs that use the color green.

Industry/Entity Type

Business

```html
<!DOCTYPE html>
<html lang="en">
<head>
<meta charset="utf-8">
<title>Lumen CELL — Business Card</title>
<link href="https://fonts.googleapis.com/css2?family=Open+Sans:wght@400;600;700&display=swap" rel="stylesheet">
<style>
  :root {
    --backdrop: #2b2b2d;
    --card: #161616;
    --green: #2fa84a;
    --green-bright: #5cc13f;
    --rule: #1f7a34;
  }
  html, body {
    margin: 0;
    padding: 0;
    width: 1200px;
    height: 1189px;
    overflow: hidden;
    background: var(--backdrop);
    font-family: "Open Sans", Arial, sans-serif;
  }
  .canvas {
    position: relative;
    width: 1200px;
    height: 1189px;
  }
  .card {
    position: absolute;
    left: 220px;
    width: 760px;
    height: 434px;
    background: var(--card);
    border-radius: 26px;
    box-shadow: 0 18px 40px rgba(0,0,0,0.55);
  }
  .card--front { top: 110px; }
  .card--back { top: 640px; }

  .brand {
    display: flex;
    align-items: center;
    gap: 18px;
    color: var(--green-bright);
    font-weight: 600;
    font-size: 64px;
    letter-spacing: -2px;
    line-height: 1;
  }
  .brand__dot {
    width: 34px;
    height: 34px;
    border-radius: 50%;
    background: var(--green-bright);
    flex: none;
  }
  .card--front .brand {
    position: absolute;
    left: 50%;
    top: 50%;
    transform: translate(-50%, -50%);
  }
  .card--back .brand {
    position: absolute;
    left: 60px;
    top: 50%;
    transform: translateY(-50%);
    font-size: 54px;
  }
  .divider {
    position: absolute;
    left: 430px;
    top: 70px;
    width: 2px;
    height: 294px;
    background: var(--rule);
  }
  .contact {
    position: absolute;
    left: 466px;
    top: 78px;
    color: var(--green);
    font-size: 19px;
    line-height: 1.3;
  }
  .contact__name {
    font-weight: 700;
    font-size: 25px;
    letter-spacing: 0.5px;
    margin: 0;
  }
  .contact__role {
    margin: 0 0 22px;
    font-weight: 600;
    color: var(--green-bright);
  }
  .contact__address { margin: 0 0 18px; color: var(--green-bright); }
  .contact__line {
    display: flex;
    align-items: center;
    gap: 10px;
    margin: 0;
    color: var(--green-bright);
  }
  .contact__line svg { width: 18px; height: 18px; flex: none; }
  .contact__line--plain { padding-left: 28px; }
  .contact__web { margin: 20px 0 0; }
</style>
</head>
<body>
<div class="canvas">
  <section class="card card--front" aria-label="Card front">
    <div class="brand"><span class="brand__dot"></span><span>Lumen CELL</span></div>
  </section>

  <section class="card card--back" aria-label="Card back">
    <div class="brand"><span class="brand__dot"></span><span>Lumen CELL</span></div>
    <div class="divider"></div>
    <div class="contact">
      <p class="contact__name">EMPLOYEE NAME</p>
      <p class="contact__role">Managing Director</p>
      <p class="contact__address">0000 your address Avenue<br>Cedar Hollow, SD 0000</p>
      <p class="contact__line">
        <svg viewBox="0 0 24 24" aria-hidden="true"><path fill="currentColor" d="M6.6 10.8a15.1 15.1 0 0 0 6.6 6.6l2.2-2.2c.3-.3.7-.4 1-.2 1.1.4 2.3.6 3.6.6.6 0 1 .4 1 1V20c0 .6-.4 1-1 1A17 17 0 0 1 3 4c0-.6.4-1 1-1h3.5c.6 0 1 .4 1 1 0 1.3.2 2.5.6 3.6.1.3 0 .7-.2 1z"/></svg>
        000-111-0000
      </p>
      <p class="contact__line contact__line--plain">abc@yourmail.com</p>
      <p class="contact__line">
        <svg viewBox="0 0 24 24" aria-hidden="true"><path fill="currentColor" d="M2 5h20v14H2zm2 2v.5l8 5 8-5V7zm0 2.9V17h16V9.9l-8 5z"/></svg>
        abc@yourweb.com
      </p>
      <p class="contact__web">www.abcyourweb.com</p>
    </div>
  </section>
</div>
</body>
</html>
```